The Green Sprout Website Design

I have hosting set up through Net Harbor but need Web Design for a new company called The Green Sprout. I am a holistic health coach helping individuals and groups achieve optimum health through the elimination of processed foods, GMOs, animal foods and chemical toxins in foods, beauty and household products and the promotion of a plant focused diet. I provide education and coaching programs to ensure success. The site should include my logo, the colors of black, white, orange and green and convey a simple, natural and friendly tone. My goal is to be a friendly resource to those who want or need to transition to a vegan lifestyle but don't want to feel judged or the need to be perfect to heal and make a difference. Progress vs perfection.
Updates

The tabs would be: Home About Services Recipes Resources (Things I Love) I.e affiliate links Contact Possibly a calendar of events As for products, they would be simple ebooks or 30 day programs delivered electronically. They are still in development. I will have a link to a free book excerpt for opting into my mailing list. You can see a site I built through my school's hosting for a basic example at Lorimpelland.example While I like the basic bones of it, I wanted something more robust and not tied to the school.

```html
<!DOCTYPE html>
<html lang="en">
<head>
<meta charset="utf-8">
<title>The Green Sprout</title>
<link rel="stylesheet" href="https://fonts.googleapis.com/css2?family=Quicksand:wght@400;500;700&family=Open+Sans:wght@400;600&display=swap">
<style>
:root{
  --black:#000000;
  --white:#ffffff;
  --green:#5aa82a;
  --green-light:#7cc242;
  --green-dark:#3f7f17;
  --orange:#f5a623;
  --orange-band:#f9ab1c;
  --text-dark:#2b2b2b;
  --text-gray:#777777;
  --wood-light:#e8c596;
}
*{margin:0;padding:0;box-sizing:border-box}
html,body{width:887px;height:1200px;overflow:hidden;background:var(--white)}
body{position:relative;font-family:"Open Sans",Arial,sans-serif;color:var(--text-dark)}
.abs{position:absolute}

/* header */
.site-header{left:0;top:0;width:887px;height:67px;background:var(--black)}
.brand{left:82px;top:13px;display:flex;align-items:center;gap:9px}
.brand-mark{width:40px;height:40px;border:3px solid var(--orange);border-radius:50%}
.brand-name{font-family:"Quicksand",sans-serif;font-weight:500;font-size:21px;color:var(--green-light)}
.main-nav{left:396px;top:27px;display:flex;gap:14px;font-family:"Quicksand",sans-serif;font-weight:700;font-size:10px;letter-spacing:.5px;text-transform:uppercase}
.main-nav a{color:var(--green-light);text-decoration:none}
.main-nav a.current{color:var(--orange)}

/* hero */
.hero{left:0;top:67px;width:887px;height:384px}
.hero-photo{position:absolute;inset:0;background:linear-gradient(100deg,var(--wood-light) 0%,#deb47e 45%,#6f8f3a 70%,#3e7a22 85%,#d9b43a 100%)}
.hero-title{left:96px;top:158px;font-family:"Quicksand",sans-serif;font-weight:700;font-size:33px;color:var(--green-light)}
.hero-text{left:96px;top:205px;width:345px;font-size:12.5px;line-height:16.5px;color:var(--text-dark)}
.btn{display:block;text-align:center;color:var(--white);text-decoration:none;font-size:10px;line-height:20px;height:21px;background:linear-gradient(var(--green-light),var(--green-dark));border-radius:2px}
.hero-btn{left:95px;top:273px;width:115px;line-height:21px;height:21px}
.slider-arrow{top:244px;width:22px;height:34px}
.slider-arrow.prev{left:31px}
.slider-arrow.next{left:830px}

/* intro */
.coach-photo{left:62px;top:480px;width:184px;height:222px;background:radial-gradient(ellipse at 50% 45%,#d9b49a 0%,#efe3da 55%,var(--white) 80%)}
.intro-title{left:260px;top:486px;width:300px;font-family:"Quicksand",sans-serif;font-weight:700;font-size:17px;line-height:21px;letter-spacing:.8px;color:var(--green)}
.intro-text{left:260px;top:582px;width:290px;font-size:9.6px;line-height:13.2px;color:var(--text-gray)}
.consult-btn{left:259px;top:676px;width:115px}
.recipes-title{left:572px;top:482px;font-family:"Quicksand",sans-serif;font-weight:500;font-size:18px;letter-spacing:.8px;color:var(--orange)}
.recipe{left:572px;width:250px;height:90px}
.recipe-thumb{position:absolute;left:0;top:0;width:87px;height:87px;border:2px solid #eee;background:radial-gradient(circle at 50% 55%,#7dbb3b 0%,#3f8a22 55%,#7a3a22 100%)}
.recipe-name{position:absolute;left:104px;top:0;font-size:10px;font-weight:400;color:var(--green)}
.recipe-text{position:absolute;left:104px;top:12px;width:122px;font-size:10px;line-height:12.4px;color:var(--text-gray)}

/* info panel */
.info-band{left:0;top:757px;width:887px;height:293px;background:var(--black)}
.footer-mark{left:158px;top:794px;width:72px;height:72px;border:4px solid var(--orange);border-radius:50%}
.footer-name{left:82px;top:877px;width:224px;text-align:center;font-family:"Quicksand",sans-serif;font-weight:500;font-size:16px;color:var(--green-light)}
.panel-text{font-size:9.6px;line-height:12.4px;color:var(--white)}
.about-text{left:82px;top:908px;width:225px}
.learn-btn{left:80px;top:966px;width:115px}
.panel-title{font-family:"Quicksand",sans-serif;font-weight:700;font-size:16.5px;letter-spacing:.8px;color:var(--orange);line-height:21px}
.news-title{left:326px;top:786px}
.news{left:326px;top:815px;width:232px}
.news p{margin-bottom:13px}
.book-title{left:572px;top:781px;width:240px}
.book-cover{left:604px;top:836px;width:166px;height:106px;background:linear-gradient(150deg,#8a5a3c 0%,#6e4530 50%,#4c8e2e 75%,#c0392b 100%);transform:skewY(-8deg);border-radius:3px}
.book-text{left:572px;top:965px;width:240px}
.download-btn{left:571px;top:1003px;width:115px}

/* social band */
.social-band{left:0;top:1050px;width:887px;height:88px;background:var(--orange-band)}
.social-title{left:0;top:1065px;width:887px;text-align:center;font-family:"Quicksand",sans-serif;font-size:16px;letter-spacing:1px;color:var(--white)}
.social-links{left:391px;top:1091px;display:flex;gap:9px}
.social-links span{display:block;width:26px;height:26px;border-radius:50%;background:rgba(255,255,255,.75)}

/* bottom */
.footer-nav{left:82px;top:1157px;display:flex;gap:14px;font-family:"Quicksand",sans-serif;font-size:11px;letter-spacing:.5px}
.footer-nav a{color:var(--text-gray);text-decoration:none}
.copyright{right:85px;top:1157px;font-family:"Quicksand",sans-serif;font-size:11px;color:var(--text-gray)}
.copyright span{color:var(--orange)}
</style>
</head>
<body>

<header class="site-header abs">
  <div class="brand abs"><span class="brand-mark"></span><span class="brand-name">The Green Sprout</span></div>
  <nav class="main-nav abs">
    <a class="current" href="#">Home</a><a href="#">About</a><a href="#">Services</a><a href="#">Recipes</a><a href="#">Resources</a><a href="#">Events</a><a href="#">Contact</a>
  </nav>
</header>

<section class="hero abs">
  <div class="hero-photo" role="img" aria-label="Fresh vegetables on a wooden board: peppers, cucumbers, radishes, greens and garlic"></div>
</section>
<h1 class="hero-title abs">A New You Is Awaiting!</h1>
<p class="hero-text abs">Lorem ipsum dolor sit amet, consectetuer adipiscing elit, sed diam nonummy nibh euismod tincidunt ut laoreet dolore magna aliquam erat volutpat.</p>
<a class="btn hero-btn abs" href="#">Read More</a>
<svg class="slider-arrow prev abs" viewBox="0 0 22 34" aria-label="Previous slide"><polyline points="18,2 4,17 18,32" fill="none" stroke="#fff" stroke-width="3"/></svg>
<svg class="slider-arrow next abs" viewBox="0 0 22 34" aria-label="Next slide"><polyline points="4,2 18,17 4,32" fill="none" stroke="#fff" stroke-width="3"/></svg>

<div class="coach-photo abs" role="img" aria-label="Health coach holding a bowl of fresh salad"></div>
<h2 class="intro-title abs">When was the last time you talked with someone about your health and received the personal attention you deserve?</h2>
<p class="intro-text abs">It's rare for anyone to get an hour to work on their nutrition and goals with a trained professional. As a Health Coach, I create a supportive environment that will enable you to achieve all of your health goals. I have studied all the major dietary theories and use practical lifestyle coaching methods to guide you in discovering which approach works best for you.</p>
<a class="btn consult-btn abs" href="#">Free Consultation</a>

<h2 class="recipes-title abs">Featured Recipes</h2>
<article class="recipe abs" style="top:516px">
  <div class="recipe-thumb" role="img" aria-label="Fresh garden salad"></div>
  <h3 class="recipe-name">Lorem ipsum dolor sit</h3>
  <p class="recipe-text">amet, consectetuer adipiscing elit, sed diam nonummy nibh euismod tincidunt ut laoreet dolore magna aliquam erat volutpat.</p>
</article>
<article class="recipe abs" style="top:627px">
  <div class="recipe-thumb" role="img" aria-label="Mixed green salad in a bowl"></div>
  <h3 class="recipe-name">Lorem ipsum dolor sit</h3>
  <p class="recipe-text">amet, consectetuer adipiscing elit, sed diam nonummy nibh euismod tincidunt ut laoreet dolore magna aliquam erat volutpat.</p>
</article>

<section class="info-band abs"></section>
<span class="footer-mark abs"></span>
<p class="footer-name abs">The Green Sprout</p>
<p class="panel-text about-text abs">Lorem ipsum dolor sit amet, consectetuer adipiscing elit, sed diam nonummy nibh euismod tincidunt ut laoreet dolore magna aliquam erat.</p>
<a class="btn learn-btn abs" href="#">Learn More</a>

<h2 class="panel-title news-title abs">Latest News</h2>
<div class="panel-text news abs">
  <p>Lorem ipsum dolor sit amet, consectetuer adipiscing elit, sed diam nonummy nibh euismod tincidunt ut laoreet dolore magna aliquam erat.</p>
  <p>Lorem ipsum dolor sit amet, consectetuer adipiscing elit, sed diam nonummy nibh euismod tincidunt ut laoreet dolore magna aliquam erat.</p>
  <p>Lorem ipsum dolor sit amet, consectetuer adipiscing elit, sed diam nonummy nibh euismod tincidunt ut laoreet dolore magna aliquam erat.</p>
</div>

<h2 class="panel-title book-title abs">Get your free nutrition book excerpt!</h2>
<div class="book-cover abs" role="img" aria-label="Nutrition ebook cover with a salad"></div>
<p class="panel-text book-text abs">Lorem ipsum dolor sit amet, consectetuer adipiscing elit, sed diam nonummy.</p>
<a class="btn download-btn abs" href="#">Download Now</a>

<section class="social-band abs"></section>
<p class="social-title abs">You can also find us on</p>
<div class="social-links abs"><span></span><span></span><span></span></div>

<nav class="footer-nav abs">
  <a href="#">Home</a><a href="#">About</a><a href="#">Services</a><a href="#">Recipes</a><a href="#">Resources</a><a href="#">Events</a><a href="#">Contact</a>
</nav>
<p class="copyright abs">© <span>The Green Sprout</span> 2014</p>

</body>
</html>
```